Professional Services - letterhead / business cards

The company (velmora holdings) will provide services to Investment Funds and large investors in Spain. I have recently chosen a logo that I am attaching.

I would like a simple stationary design that i could use as letter head, business cards and "with compliments" cards.

I am not quite sure which color I will mostly use for the logo, in the email signature I will probably lean towards the white background and grey letters. I am attaching my favourite options.

Target Market(s)

Large Multinationals, Investment funds and Law firms

Industry/Entity Type

Business

Requirements
Must have
• my details are:
Luis R. Albarda
Velmora Holdings S.L.
Casa de Valdetorres
Calle de Ortuzar Beltrán 27
28019 Madrid
T: +34 (91) 387-6051
M: +34 (655) 814-073
e-mail: lalbarda@velmoraholdings.example

```html
<!DOCTYPE html>
<html lang="en">
<head>
<meta charset="utf-8">
<title>Velmora Holdings – Business Card</title>
<link rel="stylesheet" href="https://fonts.googleapis.com/css2?family=Jost:wght@400;500;600&display=swap">
<style>
  :root {
    --navy: #262668;
    --white: #ffffff;
    --grey-text: #6f6f78;
    --grey-line: #b9b9c2;
    --backdrop: #ecebe8;
    --card-shadow: rgba(0, 0, 0, 0.18);
  }
  html, body {
    margin: 0;
    padding: 0;
    width: 1200px;
    height: 720px;
    overflow: hidden;
    background: var(--backdrop);
    font-family: "Jost", "Century Gothic", sans-serif;
  }
  .stage {
    position: relative;
    width: 1200px;
    height: 720px;
  }
  .card {
    position: absolute;
    top: 205px;
    width: 540px;
    height: 310px;
    border-radius: 28px;
    overflow: hidden;
    box-shadow: 0 6px 18px var(--card-shadow);
  }
  .card-front { left: 40px; background: var(--white); }
  .card-back { left: 620px; background: var(--navy); }

  .wordmark {
    font-weight: 400;
    letter-spacing: 0.5px;
    white-space: nowrap;
  }
  .card-front .wordmark {
    position: absolute;
    left: 38px;
    top: 34px;
    font-size: 44px;
    color: var(--navy);
  }
  .holder {
    position: absolute;
    left: 40px;
    top: 122px;
    white-space: nowrap;
  }
  .holder-name {
    font-weight: 600;
    font-size: 21px;
    letter-spacing: 1px;
    color: var(--navy);
    text-transform: uppercase;
  }
  .holder-company {
    font-size: 13px;
    color: var(--grey-text);
  }
  .contact-list {
    position: absolute;
    left: 40px;
    top: 168px;
    margin: 0;
    padding: 0;
    list-style: none;
    font-size: 13.5px;
    color: var(--grey-text);
  }
  .contact-list li {
    display: flex;
    align-items: center;
    gap: 8px;
    height: 21px;
  }
  .contact-icon { width: 12px; height: 12px; fill: var(--navy); }
  .wave {
    position: absolute;
    left: 0;
    bottom: 0;
    width: 540px;
    height: 310px;
  }
  .address {
    position: absolute;
    right: 30px;
    bottom: 22px;
    text-align: right;
    font-size: 13px;
    line-height: 17px;
    color: var(--white);
  }

  .card-back .wordmark {
    position: absolute;
    left: 0;
    right: 0;
    top: 112px;
    text-align: center;
    font-size: 46px;
    color: var(--white);
  }
  .website {
    position: absolute;
    left: 0;
    right: 0;
    bottom: 46px;
    text-align: center;
    font-size: 14px;
    font-weight: 500;
    letter-spacing: 7px;
    color: var(--white);
  }
</style>
</head>
<body>
<main class="stage">
  <section class="card card-front" aria-label="Business card, front">
    <div class="wordmark">velmora holdings</div>

    <div class="holder">
      <span class="holder-name">Luis R. Albarda,</span>
      <span class="holder-company">Velmora Holdings S.L.</span>
    </div>

    <ul class="contact-list">
      <li>
        <svg class="contact-icon" viewBox="0 0 12 12" aria-hidden="true"><path d="M2.5 0.5l2 2.5-1.2 1.2c0.7 1.6 1.9 2.8 3.5 3.5L8 6.5l2.5 2-1.3 2.5C4.5 10.5 1.5 7.5 1 2.8z"/></svg>
        +34 (91) 387-6051
      </li>
      <li>
        <svg class="contact-icon" viewBox="0 0 12 12" aria-hidden="true"><path d="M3.5 0h5a1 1 0 0 1 1 1v10a1 1 0 0 1-1 1h-5a1 1 0 0 1-1-1V1a1 1 0 0 1 1-1zm0.5 1.5v7h4v-7z"/></svg>
        +34 (655) 814-073
      </li>
      <li>
        <svg class="contact-icon" viewBox="0 0 12 12" aria-hidden="true"><path d="M0.5 2.5h11v7h-11z M1 3l5 3.5L11 3" stroke="#ffffff" stroke-width="0.8"/></svg>
        lalbarda@velmoraholdings.example
      </li>
    </ul>

    <svg class="wave" viewBox="0 0 540 310" aria-hidden="true">
      <path d="M0 268 C160 296 330 248 540 186 L540 310 L0 310 Z" fill="var(--navy)"/>
      <path d="M0 258 C160 286 330 238 540 174" fill="none" stroke="var(--grey-line)" stroke-width="3"/>
      <path d="M0 284 C170 306 345 262 540 204" fill="none" stroke="var(--white)" stroke-width="1.6"/>
    </svg>

    <address class="address">
      Casa de Valdetorres<br>
      Calle de Ortuzar Beltrán 27<br>
      28019 Madrid
    </address>
  </section>

  <section class="card card-back" aria-label="Business card, back">
    <div class="wordmark">velmora holdings</div>
    <div class="website">www.velmora.example</div>
  </section>
</main>
</body>
</html>
```